Web Design Project

We need a website design for a new website. The site will have two parts, a sales and marketing site (nothing exists at present) and an online business application, which is under construction.
The sales and marketing site needs a top level menu, and area to log into or sign up to the online applciation. Other than that we are open to suggestions.
The onlne applciations needs a similar look/feel to the marketing site and it's design needs to incorporate the following parts:
- grids
- settings page
- pop up boxes
- error messages
Please create an account on the development site at http://vorlindesk.hostpad.net to see waht functionality needs to be incorporated in the design. Needs to be viewed in FireFox.
The logo we have chosen for the site has been uploaded, please ensure all designs fit with this. I have no problems if you wish to make alterations to the logo.
- Design for both the marketing site and online application.

```html
<!DOCTYPE html>
<html lang="en">
<head>
<meta charset="utf-8">
<title>vorlindesk – Add expense</title>
<link rel="stylesheet" href="https://fonts.googleapis.com/css2?family=Open+Sans:ital,wght@0,400;0,600;0,700;1,400&display=swap">
<style>
:root{
  --header-top:#5a5a5a;
  --header-bottom:#232323;
  --page-bg:#f1f2f2;
  --panel-bg:#ffffff;
  --line:#d6d6d6;
  --line-soft:#e4e4e4;
  --text:#222222;
  --text-soft:#555555;
  --link-blue:#1c5fae;
  --link-red:#8a2a17;
  --brand-green:#5bb52a;
  --tab-blue-top:#5d9be6;
  --tab-blue-bottom:#2463c2;
  --tab-grey-top:#f5f5f5;
  --tab-grey-bottom:#d9d9d9;
  --save-top:#7fd25f;
  --save-bottom:#3a9e27;
  --cancel-top:#f47a3a;
  --cancel-bottom:#d42f08;
  --menu-hover:#e6e6e6;
}
*{box-sizing:border-box;margin:0;padding:0}
html,body{width:1200px;height:712px;overflow:hidden}
body{position:relative;background:var(--page-bg);font-family:"Open Sans",Arial,sans-serif;color:var(--text)}
.abs{position:absolute}

.site-header{left:0;top:0;width:1200px;height:136px;background:linear-gradient(var(--header-top),var(--header-bottom))}
.company{left:16px;top:54px;color:#fff;font-size:15px;font-weight:700}
.company em{font-weight:700}
.brand{left:0;width:1200px;top:34px;text-align:center;font-size:52px;font-weight:700;color:var(--brand-green);letter-spacing:-1px}

.user-box{left:1015px;top:53px;width:160px;height:36px;background:linear-gradient(#fff,#ececec);border:1px solid #c9c9c9;border-radius:4px;font-size:13px;font-weight:600;display:flex;align-items:center}
.user-box span{width:128px;text-align:center}
.user-box .arrows{position:absolute;right:0;top:0;width:32px;height:34px;border-left:1px solid #d0d0d0}
.user-menu{left:1015px;top:98px;width:160px;height:105px;background:#f8f8f8;border:1px solid #c9c9c9;border-radius:4px;box-shadow:0 2px 4px rgba(0,0,0,.15);font-size:13px;color:#444}
.user-menu li{list-style:none;height:25px;line-height:25px;padding-left:21px}
.user-menu li:first-child{margin-top:10px}
.user-menu .active{background:var(--menu-hover);color:#222}

.tabs{left:8px;top:162px;height:42px;display:flex;border:1px solid #a9a9a9;border-radius:8px;overflow:hidden;box-shadow:0 1px 2px rgba(0,0,0,.15)}
.tab{height:100%;display:flex;align-items:center;justify-content:center;font-size:16px;font-weight:600;color:#444;background:linear-gradient(var(--tab-grey-top),var(--tab-grey-bottom));border-left:1px solid #b8b8b8}
.tab.current{background:linear-gradient(var(--tab-blue-top),var(--tab-blue-bottom));color:#fff;border-left:none}

.panel{left:8px;top:223px;width:1185px;height:408px;background:var(--panel-bg);border:1px solid var(--line);border-radius:3px}
.panel-notch{left:30px;top:213px}
.filters{left:32px;top:243px;font-size:14px}
.filters .unclaimed{color:var(--link-blue)}
.filters .rejected{color:var(--link-red)}
.filters .sep{color:#999}
.divider{left:9px;top:278px;width:1183px;height:1px;background:var(--line-soft)}

.grid{left:20px;top:288px;width:1162px;height:245px;border:1px solid var(--line);border-collapse:collapse}
.grid .col{top:288px;height:245px;width:1px;background:var(--line)}
.grid-head{left:20px;top:348px;width:1162px;height:1px;background:var(--line)}
.th{top:308px;font-size:15px}
.th.sort{color:var(--link-blue)}
.cell{font-size:14px}
.label{font-size:13px;color:var(--text-soft)}
.label.strong{font-size:15px;color:var(--text);font-weight:600}
.field{height:26px;border:1px solid #bdbdbd;background:#fff;box-shadow:inset 0 1px 2px rgba(0,0,0,.1)}
.field.hint{font-size:13px;font-style:italic;color:#666;padding:5px 8px}
.select{height:27px;border:1px solid #bdbdbd;border-radius:3px;background:linear-gradient(#fff,#efefef);font-size:12px;font-style:italic;color:#444;padding:6px 10px;display:flex;justify-content:space-between;align-items:center}
.select::after{content:"";border:5px solid transparent;border-top:6px solid #555;border-bottom:0}
.browse{height:27px;width:77px;border:1px solid #7a8ea8;border-radius:3px;background:linear-gradient(#f4f8fd,#c9d6e6);font-size:13px;text-align:center;line-height:25px}
.dollar{color:var(--link-blue);font-weight:700;font-size:15px}
.check{width:14px;height:14px;border:1px solid #888;background:linear-gradient(#fff,#e4e4e4);border-radius:2px}
.btn{width:70px;height:25px;border-radius:13px;color:#fff;font-size:13px;font-weight:600;text-align:center;line-height:25px}
.btn.save{background:linear-gradient(var(--save-top),var(--save-bottom))}
.btn.cancel{background:linear-gradient(var(--cancel-top),var(--cancel-bottom))}

.add-label{left:36px;top:563px;font-size:16px;font-weight:600}
.add-select{left:150px;top:562px;width:205px;height:25px;border:1px solid #9aa9bd;background:#fff;font-size:13px;font-style:italic;color:#777;padding:3px 8px}
.add-select .drop{position:absolute;right:1px;top:1px;width:19px;height:21px;border:1px solid #7b98c2;background:linear-gradient(#eaf2fc,#bcd1ee)}
.add-list{left:150px;top:590px;width:205px;height:96px;border:1px solid #7b98c2;background:#fff;font-size:13px;padding:5px 10px;line-height:17px}
.add-list .placeholder{font-style:italic;color:#777}
</style>
</head>
<body>

<header class="site-header abs"></header>
<div class="company abs">Company : <em>q7nlabs</em></div>
<div class="brand abs">vorlindesk</div>

<div class="user-box abs"><span>Welcome user</span>
  <svg class="arrows" viewBox="0 0 32 34" aria-hidden="true"><path d="M12 15l4-5 4 5z M12 20l4 5 4-5z" fill="#888"/></svg>
</div>
<ul class="user-menu abs">
  <li>Edit Profile</li>
  <li class="active">Change Password</li>
  <li>Sign out</li>
</ul>

<nav class="tabs abs">
  <div class="tab current" style="width:138px">Add expense</div>
  <div class="tab" style="width:177px">Claim management</div>
  <div class="tab" style="width:104px">Settings</div>
  <div class="tab" style="width:180px">User management</div>
</nav>

<main>
  <div class="panel abs"></div>
  <svg class="panel-notch abs" width="22" height="12" viewBox="0 0 22 12" aria-hidden="true"><path d="M0 11L11 0 22 11" fill="#fff" stroke="#d6d6d6"/></svg>
  <div class="filters abs"><span class="unclaimed">UnClaimed (0)</span> <span class="sep">|</span> <span class="rejected">Rejected (0)</span></div>
  <div class="divider abs"></div>

  <div class="grid abs"></div>
  <div class="grid-head abs"></div>
  <div class="grid"><div class="col abs" style="left:118px"></div><div class="col abs" style="left:652px"></div><div class="col abs" style="left:763px"></div><div class="col abs" style="left:872px"></div><div class="col abs" style="left:983px"></div><div class="col abs" style="left:1090px"></div></div>

  <div class="th abs" style="left:35px">Date</div>
  <div class="th abs" style="left:132px">Description</div>
  <div class="th abs" style="left:664px">Class</div>
  <div class="th abs" style="left:774px">Client Name</div>
  <div class="th abs" style="left:885px">Project Name</div>
  <div class="th sort abs" style="left:993px">Amount</div>
  <div class="check abs" style="left:1102px;top:312px"></div>

  <div class="cell abs" style="left:35px;top:366px">29.12.2011</div>
  <div class="label strong abs" style="left:132px;top:366px">Expense :</div>
  <div class="label abs" style="left:202px;top:368px">Description :</div>
  <div class="field abs" style="left:287px;top:365px;width:119px"></div>
  <div class="label abs" style="left:419px;top:368px">Tax Amount : <span class="dollar">$</span></div>
  <div class="field abs" style="left:518px;top:365px;width:119px"></div>

  <div class="label strong abs" style="left:158px;top:421px">Payment Method :</div>
  <div class="select abs" style="left:287px;top:419px;width:119px">None</div>
  <div class="label abs" style="left:467px;top:423px">Notes :</div>
  <div class="field abs" style="left:518px;top:419px;width:119px"></div>

  <div class="label abs" style="left:223px;top:474px">Upload...</div>
  <div class="field hint abs" style="left:287px;top:470px;width:239px">Drop files here to upload</div>
  <div class="browse abs" style="left:533px;top:470px">Browse...</div>

  <div class="select abs" style="left:664px;top:365px;width:88px">None</div>
  <div class="select abs" style="left:773px;top:365px;width:89px">None</div>
  <div class="select abs" style="left:884px;top:365px;width:89px">None</div>
  <div class="select abs" style="left:992px;top:365px;width:89px">None</div>

  <div class="btn save abs" style="left:1102px;top:367px">Save</div>
  <div class="btn cancel abs" style="left:1102px;top:404px">Cancel</div>

  <div class="add-label abs">Add Expense :</div>
  <div class="add-select abs">-- Add Expense --
    <svg class="drop" viewBox="0 0 19 21" aria-hidden="true"><path d="M5 8l4.5 5L14 8" fill="none" stroke="#1f4f99" stroke-width="2"/></svg>
  </div>
  <ul class="add-list abs" style="list-style:none">
    <li class="placeholder">-- Add Expense --</li>
    <li>Travel</li>
    <li>Expense</li>
    <li>Activity</li>
    <li>Milege</li>
  </ul>
</main>

</body>
</html>
```